Professional, Modern and Clean Business Card
Brightvale Grocers & Supply Partners, Inc.
Professional, Modern and Clean Business Card - Food
Creative Brief
Simple
Dorian Whitcombe
71-14 82nd Avenue Maspeth, NY 11492
dorian@brightvalegrocers.example
www.brightvalegrocers.example
We will need 2 business cards, one for myself Dorian Whitcombe and the other Rowan Elkhart. My information is above, for Rowan Elkhart the cell is (214) 555-0193 and the email is row@brightvalegrocers.example, everything else will remain the same.
Be creative with just the logo on the back.

```html
<!DOCTYPE html>
<html lang="en">
<head>
<meta charset="utf-8">
<title>Brightvale Grocers – Business Card</title>
<link rel="stylesheet" href="https://fonts.googleapis.com/css2?family=Quicksand:wght@500;700&display=swap">
<style>
  :root {
    --brand-red: #d3202a;
    --brand-red-dark: #a8141c;
    --brand-green: #5aa532;
    --ink: #4a4a4a;
    --paper: #ffffff;
    --backdrop: #e9e9ea;
    --rule: #c9c9c9;
  }
  * { margin: 0; padding: 0; box-sizing: border-box; }
  html, body { width: 1200px; height: 871px; overflow: hidden; }
  body {
    background: var(--backdrop);
    font-family: "Quicksand", sans-serif;
    color: var(--ink);
    display: flex;
    flex-direction: column;
    align-items: center;
    justify-content: center;
    gap: 40px;
  }
  .card {
    position: relative;
    width: 640px;
    height: 366px;
    background: var(--paper);
    box-shadow: 0 2px 10px rgba(0,0,0,.12);
    overflow: hidden;
  }
  .wordmark {
    display: flex;
    align-items: center;
    gap: 10px;
    color: var(--brand-red);
    font-weight: 700;
    white-space: nowrap;
  }
  .wordmark-dot {
    width: 14px; height: 14px;
    border-radius: 50%;
    background: var(--brand-green);
    flex: none;
  }
  .card-back { display: flex; align-items: center; justify-content: center; }
  .card-back .wordmark { font-size: 46px; }

  .card-front .wordmark {
    position: absolute;
    right: 40px;
    top: 138px;
    font-size: 30px;
  }
  .holder { position: absolute; left: 40px; top: 44px; }
  .holder-name { color: var(--brand-red); font-size: 16px; font-weight: 700; }
  .holder-title { font-size: 12px; font-weight: 500; margin-top: 2px; }
  .contact-list {
    position: absolute;
    left: 40px;
    top: 104px;
    list-style: none;
    font-size: 11px;
    font-weight: 500;
    line-height: 19px;
  }
  .contact-list li { display: flex; align-items: center; gap: 8px; }
  .contact-icon {
    width: 10px; height: 10px;
    border-radius: 50%;
    background: var(--brand-red);
    flex: none;
  }
  .swoosh { position: absolute; left: 0; bottom: 0; width: 640px; height: 366px; }
</style>
</head>
<body>
  <section class="card card-back" aria-label="Card back">
    <div class="wordmark"><span class="wordmark-dot"></span>Brightvale Grocers</div>
  </section>

  <section class="card card-front" aria-label="Card front">
    <svg class="swoosh" viewBox="0 0 640 366" aria-hidden="true">
      <defs>
        <linearGradient id="band" x1="0" y1="0" x2="0" y2="1">
          <stop offset="0" stop-color="#e12a33"/>
          <stop offset="1" stop-color="#a8141c"/>
        </linearGradient>
      </defs>
      <path d="M0 292 Q300 336 640 262 L640 366 L0 366 Z" fill="url(#band)"/>
      <path d="M0 286 Q300 326 640 254" fill="none" stroke="#d9d9d9" stroke-width="2"/>
      <path d="M180 300 Q420 306 640 250" fill="none" stroke="#5aa532" stroke-width="4"/>
    </svg>

    <div class="holder">
      <p class="holder-name">Dorian Whitcombe</p>
      <p class="holder-title">Consultant</p>
    </div>
    <ul class="contact-list">
      <li><span class="contact-icon"></span>(214) 555-0100</li>
      <li><span class="contact-icon"></span>(214) 555-0193</li>
      <li><span class="contact-icon"></span>(214) 555-0147</li>
      <li><span class="contact-icon"></span>dorian@brightvalegrocers.example</li>
      <li><span class="contact-icon"></span>www.brightvalegrocers.example</li>
      <li><span class="contact-icon"></span>71-14 82nd Avenue Maspeth, NY 11492</li>
    </ul>

    <div class="wordmark"><span class="wordmark-dot"></span>Brightvale Grocers</div>
  </section>
</body>
</html>
```